Vodka label, brand name: VELVET MOOR

We are looking for a vodka label design, which will print on paper or plastic (not a bottle printing)

We are small distilling company: Copperfen Distillery. Located in Toronto, Canada. Our business is small batches of handcrafted very smooth vodka production. 40% abv. Made from cane sugar and spring water.

Our audience pretty mach everyone who consume vodka/alcohol, we are not targeting any specific group.

Back label should have barcode, government warning and this text:

Our vodka is handmade in small batches to the highest standards befitting the true vodka perfectionist. We use silk filtering process for exceptional purity, clarity, and smoothness. It is distilled 6 times from the finest organic cane sugar using only the best Canadian spring water. Discover the smooth, clear taste for yourself.
Distilled and Bottled by
Copperfen Distillery Inc.
Toronto, Canada

Government Warning: In accordance to the Surgeon General, women should not drink alcoholic beverages during pregnancy because of the risk of birth defects. Consumption of alcoholic beverages impairs your ability to drive a car or operate machinery and may cause health problems.

Size of the bottle as follows (see example in the attachment) :
Volume: 750ml
Total height: 330mm
Body diameter: 77mm
Closure: Bar Top
Silver synthetic cork

Target Market(s)

Colors

Designer to choose colors to be used in the design.

Requirements
Must have
• Incorporate the name: VELVET MOOR
• Incorporate: DISTILLED FROM ORGANIC CANE SUGAR
• Back bottle label should have barcode, government warning and this text:
• Our vodka is handmade in small batches to the highest standards befitting the true vodka perfectionist. We use silk filtering process for exceptional purity, clarity, and smoothness. It is distilled 6 times from the finest organic cane sugar using only the best Canadian spring water. Discover the smooth, clear taste for yourself.
• Distilled and Bottleb by
• Copperfen Distillery Inc.
• Toronto, Canada
• Government Warning: In accordance to the Surgeon General, women should not drink alcoholic beverages during pregnancy because of the risk of birth defects. Consumption of alcoholic beverages impairs your ability to drive a car or operate machinery and may cause health problems.
Nice to have
• 1) To show in wording or design it was Handmade
• 2) To show in wording or design it was made with Natural Spring Water
• To show in wording or design it was made in small batches
• 3) To show in wording or design it was made local in Toronto, Canada
• "The Six" "The 6ix"- is the nick name of city of Toronto that's just for designer to consider and not mandatory to implement on design
Should not have
• We try to lower cost of printing , so design should be for digital printing without Gold, Silver or any other color which requires foil application on label and will increase cost of printing.
• No copy paste from internet images. Such designs will be ignored and reported to website admin. Authentic design work only.
• Please try not to use clock or any related to that images. Its nothing to do with clock, its too naive to show 6 pm on the watches in your design. Its could be time of the day (evening), after work, the six as nick name of Toronto. But not clock or watches .

```html
<!DOCTYPE html>
<html lang="en">
<head>
<meta charset="utf-8">
<title>Velvet Moor Vodka – Labels</title>
<link href="https://fonts.googleapis.com/css2?family=Archivo+Black&family=Oswald:wght@700&family=Allura&family=EB+Garamond&family=Arimo:wght@400&display=swap" rel="stylesheet">
<style>
  :root {
    --page: #ffffff;
    --label: #111111;
    --tan: #cfa57a;
    --tan-soft: #b8946f;
    --rule: #6e5c4a;
  }
  * { margin: 0; padding: 0; box-sizing: border-box; }
  html, body { width: 1200px; height: 800px; overflow: hidden; background: var(--page); }
  .canvas {
    width: 1200px; height: 800px;
    display: flex; justify-content: center; align-items: center; gap: 90px;
  }
  .label {
    width: 400px; height: 740px;
    background: var(--label);
    color: var(--tan);
    position: relative;
  }

  /* Back label */
  .label--back {
    display: flex; flex-direction: column; justify-content: center;
    padding: 0 44px;
    font-family: "Arimo", Arial, sans-serif;
    font-size: 12.5px; line-height: 1.55;
    text-transform: uppercase;
    color: var(--tan-soft);
  }
  .back-story, .back-warning { text-align: justify; hyphens: auto; }
  .back-bottler { text-align: center; margin: 26px 0; }

  /* Front label */
  .label--front { text-align: center; }
  .brand-name {
    position: absolute; top: 112px; left: 0; right: 0;
    font-family: "Archivo Black", "Arial Black", sans-serif;
    font-size: 64px; line-height: 1.12; letter-spacing: 0.14em;
    padding-left: 0.14em;
  }
  .product-block { position: absolute; top: 318px; left: 0; right: 0; }
  .product-note {
    font-family: "Allura", cursive;
    font-size: 46px; line-height: 1;
  }
  .product-type {
    font-family: "Oswald", "Arial Narrow", sans-serif;
    font-weight: 700; font-size: 80px; line-height: 0.95;
    letter-spacing: -0.01em;
    margin-top: 2px;
  }
  .product-origin {
    font-family: "Archivo Black", "Arial Black", sans-serif;
    font-size: 17px; letter-spacing: 0.14em;
    margin-top: 2px;
  }
  .claims {
    position: absolute; top: 552px; left: 0; right: 0;
    font-family: "EB Garamond", Georgia, serif;
    font-size: 17.5px; letter-spacing: 0.02em;
  }
  .claims-line { line-height: 1.4; }
  .claims-rule {
    width: 356px; height: 1px; background: var(--rule);
    margin: 2px auto;
  }
  .volume {
    position: absolute; top: 658px; left: 0; right: 0;
    font-family: "Archivo Black", "Arial Black", sans-serif;
    font-size: 18px; letter-spacing: 0.14em;
  }
</style>
</head>
<body>
<main class="canvas">
  <section class="label label--back" aria-label="Back label">
    <p class="back-story">Our vodka is handmade in small batches to the highest standards befitting the true vodka perfectionist. We use silk filtering process for exceptional purity, clarity, and smoothness. It is distilled 6 times from the finest organic cane sugar using only the best Canadian spring water. Discover the smooth, clear taste for yourself.</p>
    <p class="back-bottler">Distilled and bottled by<br>Copperfen Distillery Inc.<br>Toronto, Canada</p>
    <p class="back-warning">Government warning: In accordance to the Surgeon General, women should not drink alcoholic beverages during pregnancy because of the risk of birth defects. Consumption of alcoholic beverages impairs your ability to drive a car or operate machinery and may cause health problems.</p>
  </section>

  <section class="label label--front" aria-label="Front label">
    <h1 class="brand-name">VELVET<br>MOOR</h1>
    <div class="product-block">
      <p class="product-note">Handmade</p>
      <p class="product-type">VODKA</p>
      <p class="product-origin">TORONTO, CANADA</p>
    </div>
    <div class="claims">
      <p class="claims-line">DISTILLED FROM ORGANIC CANE SUGAR</p>
      <div class="claims-rule"></div>
      <p class="claims-line">MADE WITH NATURAL SPRING WATER</p>
    </div>
    <p class="volume">750 ML</p>
  </section>
</main>
</body>
</html>
```